Label Design for Nuts package*

Develop the design for a label for nuts sold in a paperbag.

you can find our website here: www.brotkorn-snack.de.
Here comes the link to our catalogue: https://www.blattwerk-docs.com/de/document/read/48172095/brotkorn-premium-snacks-gesamtkatalog-2019

With this product we are targeting private customers who want to buy nuts with plastic free packaging online.
The colours of the label should fit the brown paper bag.

```html
<!DOCTYPE html>
<html lang="de">
<head>
<meta charset="utf-8">
<title>Brotkorn Premium Nuts – Label</title>
<link rel="stylesheet" href="https://fonts.googleapis.com/css2?family=Roboto+Condensed:wght@400;700&family=Roboto:wght@700&family=Alegreya+SC&display=swap">
<style>
  :root {
    --backdrop: #c8bfb7;
    --kraft: #c9a67a;
    --kraft-light: #d3b388;
    --kraft-edge: #b8935f;
    --ink-dark: #4a2418;
    --ink-brown: #6b3424;
    --ink-soft: #9a6a4c;
    --stitch: #f1ece4;
    --almond-light: #d08a52;
    --almond-dark: #8e4a22;
  }
  * { margin: 0; padding: 0; box-sizing: border-box; }
  html, body {
    width: 1200px;
    height: 900px;
    overflow: hidden;
    background: var(--backdrop);
  }
  .canvas {
    position: relative;
    width: 1200px;
    height: 900px;
  }
  .bag-front {
    position: absolute;
    left: 360px;
    top: 40px;
    width: 480px;
    height: 820px;
    background: linear-gradient(180deg, var(--kraft-light) 0%, var(--kraft) 100%);
    border: 1px solid var(--kraft-edge);
  }
  .top-seam {
    position: absolute;
    left: 0;
    top: 70px;
    width: 100%;
    height: 3px;
    border-top: 3px dashed var(--stitch);
  }
  .fold-line {
    position: absolute;
    left: 0;
    top: 120px;
    width: 100%;
    height: 1px;
    background: var(--kraft-edge);
    opacity: .5;
  }
  .brand {
    position: absolute;
    left: 0;
    top: 250px;
    width: 100%;
    text-align: center;
  }
  .brand-mark {
    display: block;
    width: 30px;
    height: 30px;
    margin: 0 auto 26px;
    border-radius: 50%;
    background: var(--ink-brown);
  }
  .brand-name {
    font-family: "Roboto Condensed", sans-serif;
    font-weight: 400;
    font-size: 58px;
    letter-spacing: 3px;
    line-height: 1;
    color: var(--ink-brown);
  }
  .brand-tagline {
    margin-top: 10px;
    font-family: "Alegreya SC", serif;
    font-size: 17px;
    letter-spacing: 3px;
    color: var(--ink-soft);
  }
  .product-name {
    position: absolute;
    left: 0;
    top: 462px;
    width: 100%;
    text-align: center;
    font-family: "Roboto Condensed", sans-serif;
    font-weight: 700;
    font-size: 42px;
    color: var(--ink-dark);
  }
  .product-weight {
    position: absolute;
    left: 0;
    top: 518px;
    width: 100%;
    text-align: center;
    font-family: "Roboto", sans-serif;
    font-weight: 700;
    font-size: 20px;
    color: var(--ink-dark);
  }
  .window {
    position: absolute;
    left: 105px;
    top: 560px;
    width: 270px;
    height: 190px;
    border-radius: 10px;
    background: radial-gradient(ellipse at 40% 40%, var(--almond-light) 0%, var(--almond-dark) 100%);
  }
</style>
</head>
<body>
  <main class="canvas">
    <section class="bag-front">
      <div class="top-seam"></div>
      <div class="fold-line"></div>

      <div class="brand">
        <span class="brand-mark"></span>
        <div class="brand-name">brotkorn</div>
        <div class="brand-tagline">PREMIUM SNACKS</div>
      </div>

      <h1 class="product-name">Premium Nuts</h1>
      <p class="product-weight">500gms</p>

      <div class="window" role="img" aria-label="Sichtfenster mit Blick auf die ganzen Mandeln im Beutel"></div>
    </section>
  </main>
</body>
</html>
```